A Weather Forecasting Site needs designs

We need a website design for our new venture which is a weather forecasting website. This website should have the latest design trends.

Menu
Weather, Maps, Videos and Photos

The home page requirements are as follows:
- Search Bar
- Local Weather
- Weather forecast of major cities in the World
Favorite locations
- Space for ADs
- Email signup

Weather Details page
This page will be redirected from the home page when you click on any of the weather forecast section

We are open to all kinds of designs and ideas. Feel free to you colors which suite your design.

```html
<!DOCTYPE html>
<html lang="en">
<head>
<meta charset="utf-8">
<title>Skycast Weather Forecast Home</title>
<link href="https://fonts.googleapis.com/css2?family=Josefin+Sans:wght@300;400;600;700&display=swap" rel="stylesheet">
<style>
:root{
  --ink:#1f1f1f;
  --muted:#8a8a8a;
  --green:#2dbb5d;
  --blue:#3a8fd9;
  --yellow:#e8b81c;
  --tan-top:#b39a80;
  --tan-bottom:#9c8670;
  --news:#6f8ea8;
  --card-shadow:0 6px 16px rgba(0,0,0,.18);
  --white:#ffffff;
}
*{margin:0;padding:0;box-sizing:border-box}
html,body{width:1200px;height:2356px;overflow:hidden;background:var(--white)}
body{position:relative;font-family:"Josefin Sans",sans-serif;color:var(--ink)}
.abs{position:absolute}

.brand{left:0;width:1200px;text-align:center;top:20px;font-size:22px;letter-spacing:2px;font-weight:600;color:var(--ink)}

.main-nav{top:79px;left:0;width:1200px;height:34px}
.nav-item{position:absolute;top:0;height:34px;display:flex;align-items:center;gap:14px;font-size:12px;color:#555}
.nav-item svg{width:16px;height:16px}
.nav-item.active{background:var(--green);color:var(--white);border-radius:17px;justify-content:center;width:157px;left:311px}

.hero{left:93px;top:129px;width:1016px;height:639px;overflow:hidden;border-radius:3px}
.hero-photo{position:absolute;inset:0 0 209px 0;background:linear-gradient(180deg,#9a8b78 0%,#7d6f5d 40%,#5d5c4d 75%,#3f4a40 100%)}
.search{left:70px;top:14px;width:327px;border-bottom:1px solid rgba(255,255,255,.8);color:rgba(255,255,255,.85);font-size:11px;padding:6px 0 5px}
.search svg{position:absolute;right:4px;top:4px}
.local-label{left:70px;top:102px;font-size:9px;letter-spacing:1.5px;color:var(--yellow)}
.city-name{left:70px;top:124px;font-size:35px;font-weight:600;color:var(--white)}
.country{left:70px;top:160px;font-size:26px;font-weight:300;color:rgba(255,255,255,.85)}
.change-loc{left:796px;top:234px;width:220px;height:56px;background:var(--blue);border-radius:28px 0 0 28px;color:var(--white);font-size:15px;display:flex;align-items:center;padding-left:28px;gap:28px}
.hero-tabs{left:0;top:388px;width:1016px;font-size:12px;letter-spacing:2px;color:var(--white)}
.hero-tab{position:absolute;top:0;display:flex;gap:18px;align-items:center}
.tab-bar{top:425px;height:6px}

.today{left:0;top:430px;width:1016px;height:209px;background:linear-gradient(180deg,var(--tan-top),var(--tan-bottom))}
.big-temp{left:72px;top:36px;font-size:112px;font-weight:600;color:var(--white);line-height:1}
.big-temp sup{font-size:52px;font-weight:400;vertical-align:top;position:relative;top:4px;margin-left:8px}
.today-label{left:62px;top:150px;font-size:9px;letter-spacing:1px;color:var(--yellow)}
.today-pill{left:62px;top:160px;width:137px;height:22px;border-radius:11px;background:rgba(60,60,60,.55);color:var(--white);font-size:13px;text-align:center;line-height:24px}
.divider{top:22px;width:1px;height:165px;background:rgba(255,255,255,.4)}
.sun-main{left:257px;top:20px}
.wind{left:257px;top:165px;font-size:13px;color:var(--white);width:120px;text-align:center;word-spacing:8px}
.days{left:425px;top:0;width:591px;height:209px;display:grid;grid-template-columns:repeat(6,1fr)}
.day{border-left:1px solid rgba(255,255,255,.22);display:flex;flex-direction:column;align-items:center;padding-top:20px;color:var(--white)}
.day-pill{background:rgba(90,80,70,.55);border-radius:10px;font-size:9px;padding:5px 10px 3px;min-width:70px;text-align:center}
.day svg{margin-top:20px}
.day-temp{margin-top:14px;font-size:16px}

.section-title{left:146px;top:850px;font-size:11px;letter-spacing:2.4px;color:#444;font-weight:600}

.skyline{left:0;top:1230px;width:1200px;height:616px;background:linear-gradient(180deg,rgba(255,255,255,1) 0%,rgba(225,225,225,.7) 40%,#c9c9c6 100%)}

.city-card{width:270px;height:355px;border-radius:8px;overflow:hidden;box-shadow:var(--card-shadow);text-align:center}
.city-card .photo{position:absolute;inset:0}
.city-card .c-name{position:relative;margin-top:34px;font-size:12px;letter-spacing:2px;color:var(--yellow)}
.city-card .c-date{position:relative;margin-top:8px;font-size:11px;letter-spacing:2px;color:#666}
.city-card.dark .c-date{color:#ccc}
.city-card .c-temp{position:relative;margin-top:20px;font-size:32px;letter-spacing:6px;color:#888;font-weight:300}
.city-card.dark .c-temp{color:#bbb}

.more{left:572px;top:1720px;width:56px;height:56px;border-radius:50%;background:rgba(255,255,255,.35);color:var(--white);font-size:20px;text-align:center;line-height:48px;letter-spacing:2px}

.newsletter{left:0;top:1846px;width:1200px;height:199px;background:linear-gradient(180deg,#7d98b0,var(--news) 60%,#7f9bb3)}
.news-title{top:40px;width:1200px;text-align:center;font-size:19px;letter-spacing:3.5px;color:var(--white);font-weight:600}
.news-text{top:70px;width:1200px;text-align:center;font-size:13px;color:var(--white)}
.news-form{left:369px;top:104px;width:464px;height:42px;border-radius:21px;overflow:hidden;display:flex;background:var(--white)}
.news-input{flex:1;font-size:13px;color:#aaa;padding:15px 0 0 36px}
.news-go{width:121px;background:var(--green);color:var(--white);font-size:18px;letter-spacing:4px;text-align:center;line-height:44px;font-weight:600}

.foot-brand{top:2124px;left:0;width:1200px;text-align:center;font-size:30px;letter-spacing:2px;font-weight:600;color:var(--ink)}
.copyright{top:2197px;width:1200px;text-align:center;font-size:11px;color:var(--muted)}
.foot-links{top:2219px;width:1200px;text-align:center;font-size:11px;color:#555;word-spacing:2px}
.socials{top:2258px;left:0;width:1200px;display:flex;justify-content:center;gap:34px}
.social{width:28px;height:28px;border-radius:50%;background:#cfcfcf}

.scroll-hint{left:1139px;top:398px;width:8px;font-size:7px;color:#666;line-height:19.5px;text-align:center}
</style>
</head>
<body>

<div class="abs brand">Skycast</div>

<nav class="abs main-nav">
  <div class="nav-item active">
    <svg viewBox="0 0 16 16" fill="none" stroke="#fff" stroke-width="1.2"><circle cx="8" cy="8" r="3"/><path d="M8 1v2M8 13v2M1 8h2M13 8h2M3 3l1.4 1.4M11.6 11.6 13 13M3 13l1.4-1.4M11.6 4.4 13 3"/></svg>
    Weather
  </div>
  <div class="nav-item" style="left:508px"><svg viewBox="0 0 16 16" fill="none" stroke="#3a8fd9"><circle cx="8" cy="8" r="6"/><path d="M5 6l3 1 3-1M6 10h4"/></svg>Maps</div>
  <div class="nav-item" style="left:660px"><svg viewBox="0 0 16 16" fill="none" stroke="#3a8fd9"><rect x="1.5" y="6" width="10" height="7" rx="1"/><path d="M11.5 8.5 15 7v5l-3.5-1.5"/><circle cx="4" cy="4" r="2"/><circle cx="9" cy="4" r="2"/></svg>Videos</div>
  <div class="nav-item" style="left:812px"><svg viewBox="0 0 16 16" fill="none" stroke="#3a8fd9"><rect x="1.5" y="4" width="13" height="9" rx="1.5"/><circle cx="8" cy="8.5" r="2.5"/><path d="M5 4l1-2h4l1 2"/></svg>Photos</div>
</nav>

<section class="abs hero">
  <div class="hero-photo" role="img" aria-label="Aerial photo of a coastal city bay with a tall rocky peak and mountains"></div>
  <div class="abs search">Search for a Loction, Place , Photo etc...
    <svg width="12" height="12" viewBox="0 0 12 12" fill="none" stroke="#fff" stroke-width="1.3"><circle cx="5" cy="5" r="3.8"/><path d="M8 8l3 3"/></svg>
  </div>
  <div class="abs local-label">LOCAL WEATHER</div>
  <h1 class="abs city-name">Rio De Janeiro</h1>
  <div class="abs country">Brazil</div>
  <div class="abs change-loc">
    <svg width="20" height="28" viewBox="0 0 20 28" fill="none" stroke="#fff" stroke-width="1.5"><path d="M10 26S2 15 2 10a8 8 0 0 1 16 0c0 5-8 16-8 16z"/><circle cx="10" cy="10" r="3"/></svg>
    Change Location
  </div>
  <div class="abs hero-tabs">
    <div class="hero-tab" style="left:60px">
      <svg width="14" height="14" viewBox="0 0 16 16" fill="none" stroke="#fff"><circle cx="8" cy="8" r="3"/><path d="M8 1v2M8 13v2M1 8h2M13 8h2M3 3l1.4 1.4M11.6 11.6 13 13M3 13l1.4-1.4M11.6 4.4 13 3"/></svg>
      <span style="font-weight:600">WEATHER</span>
    </div>
    <div class="hero-tab" style="left:360px;color:rgba(255,255,255,.8)">
      <svg width="12" height="12" viewBox="0 0 12 12" fill="none" stroke="#fff"><path d="M6 1l1.5 3.2 3.5.4-2.6 2.4.7 3.5L6 8.8 2.9 10.5l.7-3.5L1 4.6l3.5-.4z"/></svg>
      FAVORITE LOCATIONS
    </div>
  </div>
  <div class="abs tab-bar" style="left:0;width:284px;background:var(--yellow)"></div>
  <div class="abs tab-bar" style="left:284px;width:388px;background:var(--green)"></div>
  <svg class="abs" style="left:120px;top:429px" width="16" height="9"><path d="M0 0h16L8 9z" fill="#e8b81c"/></svg>

  <div class="abs today">
    <div class="abs big-temp">31<sup>°</sup></div>
    <div class="abs today-label">TODAY</div>
    <div class="abs today-pill">Monday 26<sup style="font-size:8px">th</sup></div>
    <div class="abs divider" style="left:229px"></div>
    <svg class="abs sun-main" width="120" height="120" viewBox="0 0 120 120" fill="none" stroke="#fff" stroke-width="4" stroke-linecap="round">
      <circle cx="60" cy="60" r="26"/>
      <path d="M60 8v14M60 98v14M8 60h14M98 60h14M23 23l10 10M87 87l10 10M23 97l10-10M87 33l10-10"/>
    </svg>
    <div class="abs wind">2mph / 32°</div>
    <div class="abs divider" style="left:425px;top:0;height:209px"></div>
    <div class="abs days">
      <div class="day"><span class="day-pill">Tuesday</span>
        <svg width="52" height="44" viewBox="0 0 52 44" fill="none" stroke="#fff" stroke-width="2"><circle cx="32" cy="16" r="7"/><path d="M32 3v4M43 16h4M40 7l3-3M24 7l-3-3"/><path d="M10 36a7 7 0 0 1 2-14 10 10 0 0 1 19 2 6 6 0 0 1 0 12z"/></svg>
        <span class="day-temp">25°</span></div>
      <div class="day"><span class="day-pill">Wednesday</span>
        <svg width="52" height="44" viewBox="0 0 52 44" fill="none" stroke="#fff" stroke-width="2"><path d="M10 34a8 8 0 0 1 2-16 12 12 0 0 1 23 2 7 7 0 0 1 2 14z"/></svg>
        <span class="day-temp">15°</span></div>
      <div class="day"><span class="day-pill">Thursday</span>
        <svg width="52" height="44" viewBox="0 0 52 44" fill="none" stroke="#fff" stroke-width="2"><path d="M10 28a8 8 0 0 1 2-16 12 12 0 0 1 23 2 7 7 0 0 1 2 14z"/><path d="M14 34h20M18 39h18M22 44h10"/></svg>
        <span class="day-temp">14°</span></div>
      <div class="day"><span class="day-pill">Friday</span>
        <svg width="52" height="44" viewBox="0 0 52 44" fill="none" stroke="#fff" stroke-width="2"><path d="M10 28a8 8 0 0 1 2-16 12 12 0 0 1 23 2 7 7 0 0 1 2 14z"/><path d="M18 34l-3 6M27 34l-3 6M36 34l-3 6"/></svg>
        <span class="day-temp">8°</span></div>
      <div class="day"><span class="day-pill">Saturday</span>
        <svg width="52" height="44" viewBox="0 0 52 44" fill="none" stroke="#fff" stroke-width="2"><path d="M10 28a8 8 0 0 1 2-16 12 12 0 0 1 23 2 7 7 0 0 1 2 14z"/><path d="M26 30l-4 7h6l-4 7M16 32l-2 5M36 32l-2 5"/></svg>
        <span class="day-temp">19°</span></div>
      <div class="day"><span class="day-pill">Sunday</span>
        <svg width="52" height="44" viewBox="0 0 52 44" fill="none" stroke="#fff" stroke-width="2"><circle cx="32" cy="14" r="7"/><path d="M32 2v4M43 14h4M40 6l3-3"/><path d="M10 32a7 7 0 0 1 2-14 10 10 0 0 1 19 2 6 6 0 0 1 0 12z"/><path d="M16 37l-1 4M24 37l-1 4"/></svg>
        <span class="day-temp">20°</span></div>
    </div>
  </div>
</section>

<div class="abs scroll-hint">S<br>C<br>R<br>O<br>L<br>L</div>

<h2 class="abs section-title">WEATHER FORECAST OF MAJOR CITIES IN THE WORLD</h2>

<div class="abs skyline" role="img" aria-label="Faded photo of a city skyline fading into white"></div>

<article class="abs city-card" style="left:143px;top:916px">
  <div class="photo" role="img" aria-label="City skyline with a tall art deco tower" style="background:linear-gradient(180deg,#f3f1ee 0%,#e6e2dc 35%,#a89580 70%,#6b5c4c 100%)"></div>
  <div class="c-name">NEW YORK CITY</div><div class="c-date">MONDAY | 26TH | 23:21</div><div class="c-temp">29°</div>
</article>
<article class="abs city-card" style="left:467px;top:916px">
  <div class="photo" role="img" aria-label="Iron lattice tower beside a river with boats" style="background:linear-gradient(180deg,#f4f4f4 0%,#dcdcdc 45%,#8c9384 75%,#6e7068 100%)"></div>
  <div class="c-name">PARIS CITY</div><div class="c-date">MONDAY | 26TH | 23:21</div><div class="c-temp">29°</div>
</article>
<article class="abs city-card dark" style="left:790px;top:916px">
  <div class="photo" role="img" aria-label="Suspension bridge lit at night" style="background:linear-gradient(180deg,#2d2f35 0%,#3a3834 45%,#8a5a22 70%,#2a2a2a 100%)"></div>
  <div class="c-name">SAN FRANSISCO</div><div class="c-date">MONDAY | 26TH | 23:21</div><div class="c-temp">29°</div>
</article>
<article class="abs city-card" style="left:143px;top:1318px">
  <div class="photo" role="img" aria-label="Gothic clock tower against a pale sky" style="background:linear-gradient(160deg,#5a615f 0%,#b9bcb6 40%,#d9dad6 60%,#7d6a4c 100%)"></div>
  <div class="c-name">HAKONE-MACHI</div><div class="c-date">MONDAY | 26TH | 23:21</div><div class="c-temp">29°</div>
</article>
<article class="abs city-card dark" style="left:467px;top:1318px">
  <div class="photo" role="img" aria-label="Ancient stone amphitheatre arches" style="background:linear-gradient(180deg,#4a4643 0%,#6e655c 50%,#3d3a37 100%)"></div>
  <div class="c-name">HAKONE-MACHI</div><div class="c-date">MONDAY | 26TH | 23:21</div><div class="c-temp">29°</div>
</article>
<article class="abs city-card dark" style="left:790px;top:1318px">
  <div class="photo" role="img" aria-label="Night city waterfront with a lit bridge and towers" style="background:linear-gradient(180deg,#2a2c34 0%,#3f3a45 45%,#6b3b35 75%,#1e2026 100%)"></div>
  <div class="c-name">HAKONE-MACHI</div><div class="c-date">MONDAY | 26TH | 23:21</div><div class="c-temp">29°</div>
</article>

<div class="abs more">···</div>

<section class="abs newsletter" role="img" aria-label="Blue toned lake with mountains in the background">
  <h2 class="abs news-title">SIGN UP TO OUR EMAIL NEWSLETTER</h2>
  <p class="abs news-text">Lorem ipsum dolor sit amet, consectetur adipisicing elit, sed do eiusmod tempor incididunt ut labore et dolore</p>
  <div class="abs news-form"><div class="news-input">Email Adress...</div><div class="news-go">GO</div></div>
</section>

<footer>
  <div class="abs foot-brand">Skycast</div>
  <p class="abs copyright">© 2017 Weather Website, Inc</p>
  <p class="abs foot-links">Terms* | Privacy and Policy | Contact Us</p>
  <div class="abs socials">
    <span class="social"></span><span class="social"></span><span class="social"></span>
    <span class="social"></span><span class="social"></span><span class="social"></span>
  </div>
</footer>

</body>
</html>
```